International Trading Company, 'KIRO' needs a Business Card

The company name is "KIRO" and it has own logo design.
I'd like to use its logo on this business card.
I need two side Business Card.
I'll look forward to your great design.
Thank you very much in advance.

Contact Information for Business Card

Company Name : Kiro Harbour Limited
Information Example
Dorian Pallister
Mobile(use icon please) : 1 (212) 555-0143
Tel(use icon please) : 1 (212) 555-0178
Email(use icon please) : dorian27@kiroharbour-mail.com
Address(use icon please) : 482 Halden Ave, New York, NY 10160, USA

```html
<!DOCTYPE html>
<html lang="en">
<head>
<meta charset="utf-8">
<title>Kiro Harbour Limited – Business Card</title>
<link rel="stylesheet" href="https://fonts.googleapis.com/css2?family=Montserrat:wght@400;500;800&display=swap">
<style>
  :root {
    --backdrop: #b8d3d6;
    --card-black: #050505;
    --band-grey: #4b4b4b;
    --mark-grey: #6a6a6a;
    --ink-dark: #151515;
    --url-grey: #5c5c5c;
    --card-w: 500px;
    --card-h: 286px;
  }
  * { margin: 0; padding: 0; box-sizing: border-box; }
  html, body {
    width: 1200px;
    height: 800px;
    overflow: hidden;
    background: var(--backdrop);
    font-family: "Montserrat", Arial, sans-serif;
  }
  .card-pair {
    position: absolute;
    inset: 0;
    display: flex;
    align-items: center;
    justify-content: center;
    gap: 60px;
  }
  .card {
    position: relative;
    width: var(--card-w);
    height: var(--card-h);
    background: var(--card-black);
    overflow: hidden;
  }
  .wordmark {
    position: absolute;
    left: 0;
    right: 0;
    text-align: center;
    color: var(--mark-grey);
    font-weight: 800;
    line-height: 1;
  }
  .wordmark .wordmark-name {
    display: block;
    font-size: 64px;
    letter-spacing: 4px;
  }
  .wordmark .wordmark-sub {
    display: block;
    font-size: 13px;
    letter-spacing: 2.5px;
    margin-top: 4px;
  }
  .card-back .wordmark { top: 92px; }
  .web-address {
    position: absolute;
    right: 46px;
    bottom: 26px;
    font-size: 9px;
    letter-spacing: 3px;
    color: var(--url-grey);
  }
  .card-front .wordmark { top: 40px; }
  .contact-band {
    position: absolute;
    left: 0;
    right: 0;
    bottom: 0;
    height: 108px;
    background: var(--band-grey);
    display: grid;
    grid-template-columns: 130px 150px minmax(0, 1fr);
    grid-template-rows: 24px 24px;
    row-gap: 6px;
    align-items: center;
    padding: 18px 16px 0 20px;
    color: var(--ink-dark);
    font-size: 8.5px;
    font-weight: 500;
  }
  .holder-name {
    font-size: 14px;
    font-weight: 500;
    color: var(--ink-dark);
    white-space: nowrap;
  }
  .contact-item {
    display: flex;
    align-items: center;
    gap: 7px;
    white-space: nowrap;
  }
  .contact-item svg {
    width: 11px;
    height: 11px;
    flex: none;
    fill: var(--ink-dark);
  }
  .contact-address { grid-column: 2 / 4; }
</style>
</head>
<body>
<main class="card-pair">

  <section class="card card-front" aria-label="Business card front">
    <div class="wordmark">
      <span class="wordmark-name">KIRO</span>
      <span class="wordmark-sub">HARBOUR LIMITED</span>
    </div>
    <div class="contact-band">
      <p class="holder-name">Dorian Pallister</p>
      <p class="contact-item">
        <svg viewBox="0 0 12 12" aria-hidden="true"><path d="M2.5.5 4.3 2.9 3.3 4.3c.7 1.6 2.4 3.3 4.4 4.4l1.4-1 2.4 1.8-.9 1.9C6.5 11.4.6 5.5.6 1.4z"/></svg>
        1 (212) 555-0178
      </p>
      <p class="contact-item">
        <svg viewBox="0 0 12 12" aria-hidden="true"><path d="M.5 2h11v8H.5zm1.2 1 4.3 3.4L10.3 3zm-.2 1v5h9V4L6 7.6z"/></svg>
        dorian27@kiroharbour-mail.com
      </p>
      <p class="contact-item">
        <svg viewBox="0 0 12 12" aria-hidden="true"><path d="M3 0h6a1 1 0 0 1 1 1v10a1 1 0 0 1-1 1H3a1 1 0 0 1-1-1V1a1 1 0 0 1 1-1zm0 1.5v7.5h6V1.5zM6 9.6a.8.8 0 1 0 0 1.6.8.8 0 0 0 0-1.6z"/></svg>
        1 (212) 555-0143
      </p>
      <p class="contact-item contact-address">
        <svg viewBox="0 0 12 12" aria-hidden="true"><path d="M6 0a4 4 0 0 1 4 4c0 3-4 8-4 8S2 7 2 4a4 4 0 0 1 4-4zm0 2.4a1.6 1.6 0 1 0 0 3.2 1.6 1.6 0 0 0 0-3.2z"/></svg>
        482 Halden Ave, New York, NY 10160, USA
      </p>
    </div>
  </section>

  <section class="card card-back" aria-label="Business card back">
    <div class="wordmark">
      <span class="wordmark-name">KIRO</span>
      <span class="wordmark-sub">HARBOUR LIMITED</span>
    </div>
    <p class="web-address">www.kiroharbour-trade.com</p>
  </section>

</main>
</body>
</html>
```